Wedding Invitation and envelope package

I need the 1st of many invitation designs. This is a floral collection and I have attached many designs that I like from competitors. I think that the pastel look is the best but I am hoping you can make something special. The font selection is just as important as the imagery. The overall size with bleeds is 5.25 x 7.25" and I have attached a sample to make sure sizing is clear. I also need A7 envelopes to go with the invitation, front and back flap. I want someone to look at the design and say they would pick it over any of the samples. I will need 8 total floral designs done over the next few weeks after this 1st one is done. I will also need a collection of 8 modern designs done. Please ask any questions

Font styles to use
Serif
Sans Serif
Script

Requirements
Must have
• This is a single sided invitation, a back side is not needed.
Should not have
• No full solid dark backgrounds

```html
<!DOCTYPE html>
<html lang="en">
<head>
<meta charset="utf-8">
<title>Clara &amp; Daniel – Evening Reception Invitation</title>
<link rel="stylesheet" href="https://fonts.googleapis.com/css2?family=Cinzel:wght@400;700&family=Pinyon+Script&display=swap">
<style>
  :root {
    --paper: #ffffff;
    --ink: #2f2f31;
    --band: #dbe9f5;
    --band-edge: #cfe0ef;
    --petal-blue: #9cc6ec;
    --petal-deep: #6fa6d8;
    --leaf: #9bc75a;
    --blush: #f2a48f;
  }
  * { margin: 0; padding: 0; box-sizing: border-box; }
  html, body { width: 855px; height: 1200px; overflow: hidden; background: var(--paper); }
  .invitation {
    position: relative;
    width: 855px;
    height: 1200px;
    background: var(--paper);
    color: var(--ink);
    font-family: "Cinzel", "Times New Roman", serif;
    overflow: hidden;
  }
  .wreath {
    position: absolute;
    left: 82px; top: 82px;
    width: 520px; height: 520px;
  }
  .bloom-cluster {
    position: absolute;
    left: 430px; top: 10px;
    width: 380px; height: 300px;
    border-radius: 48% 52% 45% 55%;
    background: radial-gradient(ellipse at 55% 40%, var(--petal-blue) 0%, #b9d8f2 55%, rgba(185,216,242,0) 75%);
  }
  .sprig {
    position: absolute;
    border-radius: 50%;
  }
  .sprig--left {
    left: 40px; top: 1035px; width: 90px; height: 75px;
    background: radial-gradient(ellipse, #b8d889 0%, rgba(184,216,137,0) 72%);
  }
  .sprig--right {
    left: 720px; top: 1070px; width: 100px; height: 70px;
    background: radial-gradient(ellipse, #f6b9a8 0%, rgba(246,185,168,0) 72%);
  }
  .couple {
    position: absolute;
    left: 142px; top: 140px;
    width: 400px;
    text-align: center;
  }
  .couple__first {
    display: block;
    font-size: 60px;
    font-weight: 700;
    letter-spacing: 4px;
    line-height: 1;
  }
  .couple__last {
    display: block;
    font-size: 24px;
    letter-spacing: 5px;
    margin-top: 22px;
  }
  .couple__amp {
    display: block;
    font-family: "Pinyon Script", cursive;
    font-size: 78px;
    line-height: 1;
    margin: 16px 0 4px;
  }
  .details {
    position: absolute;
    left: 63px; top: 620px;
    width: 763px; height: 520px;
    background: var(--band);
    border-radius: 6px 14px 8px 12px;
    box-shadow: inset 0 0 0 3px var(--band-edge);
    text-align: center;
    padding-top: 52px;
  }
  .details p {
    font-size: 20px;
    letter-spacing: 2.5px;
    line-height: 1;
    margin-bottom: 36px;
  }
  .details .script {
    font-family: "Pinyon Script", cursive;
    font-size: 40px;
    letter-spacing: 0.5px;
    margin-bottom: 24px;
  }
  .details .script--closing { font-size: 38px; margin-top: -6px; }
</style>
</head>
<body>
  <main class="invitation">
    <svg class="wreath" viewBox="0 0 520 520" role="img" aria-label="Circular wreath of small pastel flowers and green leaves">
      <defs>
        <linearGradient id="wreathTone" x1="0" y1="0" x2="1" y2="1">
          <stop offset="0" stop-color="#b8d889"/>
          <stop offset="0.5" stop-color="#f4b7a6"/>
          <stop offset="1" stop-color="#aacfee"/>
        </linearGradient>
      </defs>
      <circle cx="260" cy="260" r="238" fill="none" stroke="url(#wreathTone)" stroke-width="22" stroke-opacity="0.7"/>
    </svg>

    <div class="bloom-cluster" role="img" aria-label="Watercolour cluster of large pale blue flowers with green leaves"></div>

    <header class="couple">
      <span class="couple__first">CLARA</span>
      <span class="couple__last">WHITMORE</span>
      <span class="couple__amp">&amp;</span>
      <span class="couple__first">DANIEL</span>
      <span class="couple__last">HARTLEY</span>
    </header>

    <section class="details">
      <p>Request the pleasure of</p>
      <p class="script">Sophie and Thomas</p>
      <p>To join them to celebrate their marriage</p>
      <p>At an evening reception</p>
      <p>Saturday 18th April at 7.30pm</p>
      <p>At Ashdown Manor</p>
      <p>Meadow Lane, Hartfield TN7 4QR</p>
      <p class="script script--closing">Followed by dinner and dancing</p>
    </section>

    <div class="sprig sprig--left" role="img" aria-label="Small green leaf sprig"></div>
    <div class="sprig sprig--right" role="img" aria-label="Small cluster of peach blossoms"></div>
  </main>
</body>
</html>
```